Basic / Quick Business Card

Quick easy design project!

Need a one sided basic business card that matches font & style of brand and bottle label for our gourmet condiment, Velvet Corwin Sauce. Velvet Corwin Sauce is sold in specialty retail, gourmet groceries and appears on chef-driven restaurant menus, so the target market is a high end, gourmet, artisan-made food-loving customer.

Files Included:
Sauce Bottle Label
Velvet Corwin Sauce Round Logos

**About the logos - the logo may be used in a circle or alone vertically as on side of the bottle label**

Layout of Card:
May be vertical or horizontal based on designer ideas.

Logo usage (in circle vs. stand alone vertical logo) is up to designers descretion as well.

Reverse side of business card will be various high end / professional product photos / food shots using us.zelk.com system. **Designer on this project will NOT design a reserve for the card.**

Paper that will be used for printing:
Zelk Classic - it's a WHITE paper, but we use a cream background on Velvet Corwin Sauce branding, so please take this into account on design to stay brand consistent.

Elements & Copy for Card:
1. Logo in either script horizontal or vertical version
2. Copy: "Artisan Made - Small Batch"
3. Name - Rory Whitlock
4. Title - Creator
5. Phone - xxx.xxx.xxxx
6. xxxx@velvetcorwin.com
7. URL: velvetcorwinsauce.com
8. Social Media: @getvelvetcorwin on Twitter / Facebook / Instagram

Please provide final files in Illustrator or InDesign format.

```html
<!DOCTYPE html>
<html lang="en">
<head>
<meta charset="utf-8">
<title>Velvet Corwin Sauce – Business Card</title>
<link rel="stylesheet" href="https://fonts.googleapis.com/css2?family=Ubuntu:wght@400;500&family=Tinos&display=swap">
<style>
  :root {
    --page: #ece9e2;
    --card: #2b2a2a;
    --cream: #e9ebd6;
    --gold: #f2b51c;
    --ink: #4a4a4a;
    --social: #6b6f7a;
  }
  * { margin: 0; padding: 0; box-sizing: border-box; }
  html, body { width: 869px; height: 1200px; overflow: hidden; background: var(--page); }
  .canvas { position: relative; width: 869px; height: 1200px; }
  .card {
    position: absolute; left: 119px; top: 48px; width: 630px; height: 1103px;
    background: var(--card);
  }
  .brand-seal {
    position: absolute; left: 115px; top: 77px; width: 370px; height: 370px;
    border-radius: 50%; background: var(--cream); border: 12px solid var(--gold);
    display: flex; align-items: center; justify-content: center; text-align: center;
  }
  .brand-name {
    font-family: "Ubuntu", sans-serif; font-weight: 500; font-size: 54px;
    line-height: 1.05; color: var(--card);
  }
  .contact-panel {
    position: absolute; left: 63px; top: 479px; width: 525px; height: 578px;
    background: var(--cream); color: var(--ink);
    font-family: "Ubuntu", sans-serif; text-align: center;
  }
  .contact-panel > * { position: absolute; left: 0; right: 0; }
  .person { top: 78px; font-size: 38px; font-weight: 500; }
  .person .role { font-size: 30px; }
  .divider { left: 21px; right: 21px; border-top: 5px dotted var(--gold); }
  .divider--one { top: 153px; }
  .divider--two { top: 359px; }
  .divider--three { top: 466px; }
  .contact-line {
    display: flex; align-items: center; justify-content: center; gap: 10px;
    font-size: 31px;
  }
  .contact-line svg { width: 26px; height: 26px; fill: var(--ink); flex: none; }
  .contact-phone { top: 208px; }
  .contact-email { top: 254px; }
  .contact-web { top: 300px; }
  .follow {
    top: 390px; display: flex; align-items: center; justify-content: center; gap: 10px;
    font-size: 32px;
  }
  .social-dot { width: 38px; height: 38px; border-radius: 50%; background: var(--social); display: inline-block; }
  .social-dot:first-of-type { margin-left: 6px; }
  .tagline { top: 505px; font-family: "Tinos", serif; font-size: 29px; }
</style>
</head>
<body>
<div class="canvas">
  <div class="card">
    <div class="brand-seal">
      <div class="brand-name">Velvet<br>Corwin<br>Sauce</div>
    </div>
    <div class="contact-panel">
      <p class="person">Rory Whitlock<span class="role">, Creator</span></p>
      <div class="divider divider--one"></div>
      <p class="contact-line contact-phone">
        <svg viewBox="0 0 24 24" aria-hidden="true"><path d="M6.6 10.8a15.1 15.1 0 0 0 6.6 6.6l2.2-2.2a1 1 0 0 1 1-.25 11.4 11.4 0 0 0 3.6.57 1 1 0 0 1 1 1V20a1 1 0 0 1-1 1A17 17 0 0 1 3 4a1 1 0 0 1 1-1h3.5a1 1 0 0 1 1 1c0 1.25.2 2.45.57 3.6a1 1 0 0 1-.25 1z"/></svg>
        555-014-2290
      </p>
      <p class="contact-line contact-email">
        <svg viewBox="0 0 24 24" aria-hidden="true"><path d="M2 6h20v12H2z M3.5 7.5 12 13l8.5-5.5" fill="none" stroke="#4a4a4a" stroke-width="2"/></svg>
        rwhitlock@velvetcorwin.com
      </p>
      <p class="contact-line contact-web">
        <svg viewBox="0 0 24 24" aria-hidden="true" fill="none" stroke="#4a4a4a" stroke-width="2"><circle cx="12" cy="12" r="9"/><path d="M3 12h18M12 3c3 3 3 15 0 18M12 3c-3 3-3 15 0 18"/></svg>
        www.velvetcorwinsauce.com
      </p>
      <div class="divider divider--two"></div>
      <p class="follow">Follow Us On
        <span class="social-dot"></span><span class="social-dot"></span><span class="social-dot"></span>
      </p>
      <div class="divider divider--three"></div>
      <p class="tagline">Artisan Made - Small Batch</p>
    </div>
  </div>
</div>
</body>
</html>
```